Yard sign

I want it to look similar to this one,

change name to DRAVEK and submit new ideas

Also would like to improvise a bit. let's not make exactly the same thing

would like to change to: Connecticut #1 Company

also change phone to 203-555-0147
and website to
dravekllc.com

this is yard sign. size is 24' Width and 32' Height

Target Market(s)

Roof

Industry/Entity Type

Roofing

Requirements
Must have
• similar colors or add something new

```html
<!DOCTYPE html>
<html lang="en">
<head>
<meta charset="utf-8">
<title>Dravek Roofing Yard Sign</title>
<link rel="stylesheet" href="https://fonts.googleapis.com/css2?family=Montserrat:wght@900&family=Roboto+Condensed:wght@700;900&family=Roboto:wght@400&display=swap">
<style>
  :root {
    --sign-yellow-warm: #f9b91b;
    --sign-yellow-bright: #f9e21b;
    --sign-red: #e00a16;
    --sign-red-light: #e33a26;
    --sign-red-dark: #c21717;
    --sign-red-shadow: #9e1616;
    --sign-black: #000000;
    --sign-white: #ffffff;
    --sign-grey: #d9d9d9;
  }
  html, body {
    margin: 0;
    padding: 0;
    overflow: hidden;
    background: var(--sign-white);
  }
  .yard-sign {
    display: block;
    width: 900px;
    height: 1200px;
  }
  .headline-state {
    font-family: "Montserrat", sans-serif;
    font-weight: 900;
    font-size: 50px;
    fill: var(--sign-red);
  }
  .headline-rank {
    font-family: "Montserrat", sans-serif;
    font-weight: 900;
    font-size: 150px;
    fill: var(--sign-white);
    letter-spacing: -4px;
  }
  .headline-company {
    font-family: "Montserrat", sans-serif;
    font-weight: 900;
    font-size: 70px;
    fill: var(--sign-white);
  }
  .roof-line {
    fill: none;
    stroke-linecap: round;
    stroke-linejoin: round;
  }
  .service-word {
    font-family: "Montserrat", sans-serif;
    font-weight: 900;
    font-size: 236px;
    fill: var(--sign-black);
    stroke: var(--sign-white);
    stroke-width: 6px;
    paint-order: stroke;
    letter-spacing: -6px;
  }
  .brand-name {
    font-family: "Roboto Condensed", sans-serif;
    font-weight: 900;
    font-size: 222px;
    fill: var(--sign-white);
    letter-spacing: -4px;
  }
  .phone-number {
    font-family: "Roboto Condensed", sans-serif;
    font-weight: 700;
    font-size: 78px;
    fill: var(--sign-black);
    letter-spacing: -1px;
  }
  .web-address {
    font-family: "Roboto", sans-serif;
    font-weight: 400;
    font-size: 56px;
    fill: var(--sign-white);
  }
</style>
</head>
<body>
<svg class="yard-sign" viewBox="0 0 900 1200" xmlns="http://www.w3.org/2000/svg">
  <defs>
    <linearGradient id="yellow-field" x1="0" y1="0" x2="1" y2="0">
      <stop offset="0" stop-color="var(--sign-yellow-warm)"/>
      <stop offset="1" stop-color="var(--sign-yellow-bright)"/>
    </linearGradient>
  </defs>

  <!-- upper field -->
  <rect class="upper-field" x="45" y="51" width="810" height="648" fill="url(#yellow-field)"/>
  <!-- lower field -->
  <rect class="lower-field" x="45" y="697" width="810" height="458" fill="var(--sign-black)"/>

  <!-- ribbon tail folding behind -->
  <polygon class="ribbon-tail" points="0,279 98,268 112,352 289,334 300,444 0,481" fill="var(--sign-red-dark)"/>
  <polygon class="ribbon-fold" points="112,352 289,334 300,444" fill="var(--sign-red-shadow)"/>

  <!-- state label ribbon -->
  <polygon class="state-ribbon" points="49,96 611,28 600,75 622,121 60,187" fill="var(--sign-white)"/>
  <polygon class="state-ribbon-fold" points="60,187 98,191 98,215" fill="var(--sign-grey)"/>
  <text class="headline-state" x="128" y="146" transform="rotate(-7 128 146)">CONNECTICUT</text>

  <!-- red arrow banner: #1 COMPANY -->
  <polygon class="rank-banner" points="98,191 808,71 894,159 832,268 112,352" fill="var(--sign-red)"/>
  <polygon class="rank-banner-sheen" points="98,191 808,71 105,283" fill="var(--sign-red-light)" opacity="0.8"/>
  <text class="headline-rank" x="140" y="330" transform="rotate(-7 140 330)">#1</text>
  <text class="headline-company" x="370" y="282" transform="rotate(-7 370 282)">COMPANY</text>

  <!-- roof outline above the service word -->
  <polyline class="roof-line" points="330,458 548,366 790,412" stroke="var(--sign-white)" stroke-width="26"/>
  <polyline class="roof-line" points="330,458 548,366 790,412" stroke="var(--sign-black)" stroke-width="16"/>
  <rect class="roof-chimney" x="660" y="356" width="30" height="50" fill="var(--sign-black)" stroke="var(--sign-white)" stroke-width="3" transform="rotate(-7 675 381)"/>

  <!-- service word -->
  <text class="service-word" x="92" y="680" transform="rotate(-7 92 680)">ROOF</text>

  <!-- direction arrow -->
  <polygon class="direction-arrow" points="338,675 731,626 724,574 876,651 746,759 742,712 347,761" fill="var(--sign-red)" stroke="var(--sign-white)" stroke-width="3"/>

  <!-- brand -->
  <text class="brand-name" x="450" y="949" text-anchor="middle">DRAVEK</text>

  <!-- phone bar -->
  <rect class="phone-bar" x="139" y="974" width="628" height="69" fill="url(#yellow-field)"/>
  <g class="phone-icon" transform="translate(231 1009)">
    <circle r="28" fill="none" stroke="var(--sign-black)" stroke-width="4"/>
    <path d="M-13,-14 l7,-3 l6,10 l-5,4 q3,8 10,12 l4,-5 l10,6 l-3,7 q-6,5 -16,-2 q-12,-9 -16,-19 q-2,-6 3,-10z" fill="var(--sign-black)"/>
    <path d="M4,-14 q10,2 12,12 M4,-21 q16,3 19,19" fill="none" stroke="var(--sign-black)" stroke-width="2.5" stroke-linecap="round"/>
  </g>
  <text class="phone-number" x="268" y="1036">203-555-0147</text>

  <!-- web address -->
  <text class="web-address" x="450" y="1114" text-anchor="middle">www.dravekllc.com</text>
</svg>
</body>
</html>
```